Hardware Brand Packaging Design Project

We require a design for packaging for products in the retail hardware range. Initially this will be for a set of header cards for abrasive sanding discs but we plan to add other items to the range so we are looking for a range of brand elements that can be extended to other types of packaging.
The brand name is "Lumen Ridge" and we are looking for a black or dark grey background with a subtle fine pattern to break up the solid colour. This part of the design needs to be 'expandable' so that it can be used on different pack sizes as we increase the range. Two highlight or complimentary colours will add a bit of impact and become part of the brand style.
For printing purposes we have allowed for 4 colour process plus two spot colours and we have attached one of the header card dielines as a guide.
Target Market(s)
Home owners of both gender in the 25 to 55 age range
Industry/Entity Type
Printing
Requirements
Must have
- *The brand name "Lumen Ridge" should appear in the top left hand corner and we had in mind that the word would be a shiny metal / chrome appearance in could be in the shape of a shield or spear point but are open to any other suggestions.The word can be on one line or one above the other.
*Between the bottom of the hanger hole and the edge of the card is the words ABRASIVES & ACCESSORIES
*We want a performance guarantee device circle / seal or other in the bottom left quartile of the front facing panel. Circle device on attachment shows approx position.
* The right hand 25mm of the card is to be devoted to specific information about the product in the pack. This will be done by an adhered over-sticker ( see attached die-line No 2 )
* 3 line address panel or rear of card - QRV Abrasives, 456 Lane, West Auckland, New Zealand.
* Also somewhere on rear panel "Cut, Quality Checked & Packed in New Zealand from imported materials."
Nice to have
- It would be good, but not essential, to see a rough mock-up of how this design would transfer across to a box approx 80mm across the front, 100mm deep and 250mm high.

```html
<!DOCTYPE html>
<html lang="en">
<head>
<meta charset="utf-8">
<title>Lumen Ridge – Header Card Range</title>
<link href="https://fonts.googleapis.com/css2?family=PT+Sans:wght@400;700&family=Cinzel:wght@700&display=swap" rel="stylesheet">
<style>
  :root{
    --page:#ffffff;
    --card-dark:#1a1a1a;
    --card-mid:#3a3a3a;
    --chrome:#d6d6d6;
    --gold:#b8893a;
    --gold-light:#e0b45e;
    --die-pink:#e0218a;
    --fold-green:#9acd32;
    --fold-red:#d2232a;
    --grade-yellow:#fbb016;
    --grade-orange:#f47b20;
    --grade-red:#ed1c24;
    --grade-teal:#3bbcb6;
    --grade-purple:#7f3f98;
    --grade-magenta:#e2127a;
    --ink:#231f20;
  }
  *{box-sizing:border-box;margin:0;padding:0}
  html,body{width:1200px;height:766px;overflow:hidden;background:var(--page)}
  body{position:relative;font-family:"PT Sans",sans-serif;color:var(--ink)}
  .sheet-title{position:absolute;left:18px;top:10px;font-size:11px;font-weight:700;color:#555}
  .sheet-title span{font-weight:400}
  .sticker-label{position:absolute;left:474px;top:56px;font-size:11px;font-weight:700}
  .header-card{position:absolute}
  .header-card svg{display:block;width:100%;height:100%}
  .card-flat{left:58px;top:42px;width:337px;height:311px}
  .card-a{left:50px;top:410px;width:353px;height:327px}
  .card-b{left:428px;top:410px;width:353px;height:327px}
  .card-c{left:805px;top:410px;width:353px;height:327px}

  .sticker{position:absolute;width:102px;height:268px;background:var(--grade);
    border:1px solid rgba(0,0,0,.15);display:flex;flex-direction:column;padding:0 6px;color:var(--ink)}
  .sticker.on-card{width:110px;height:266px;color:#fff}
  .sticker.on-card.light{color:var(--ink)}
  .sticker.dark-text{color:var(--ink)}
  .sticker.white-text{color:#fff}
  .sticker-info{margin-top:23px;height:25px;border:1px solid currentColor;transform:rotate(180deg);
    font-size:7.5px;line-height:10px;padding:1px 4px;text-align:right;font-weight:700}
  .sticker-code-area{height:80px}
  .grade{display:flex;align-items:center;justify-content:center;gap:4px;height:30px;font-size:23px;font-weight:700;color:#fff}
  .grade-ring{width:18px;height:18px;border:2px solid #fff;border-radius:50%;box-shadow:inset 0 0 0 2px var(--grade),inset 0 0 0 3.5px #fff}
  .grade-rule{height:2px;background:#fff;margin:3px 0 5px}
  .sticker-desc{border:1px solid currentColor;height:30px;font-size:11px;line-height:12px;text-align:center;padding-top:2px}
  .sticker-desc b{display:block}
  .sticker-notes{border:1px solid currentColor;height:47px;margin-top:4px}
  .sticker-qty{margin-top:auto;margin-bottom:4px;text-align:right;font-size:9px}
  .on-card .grade{font-size:24px}
</style>
</head>
<body>

<div class="sheet-title">LUMEN RIDGE <span>pro3</span></div>

<!-- Flat header card -->
<div class="header-card card-flat">
  <svg viewBox="0 0 340 320" preserveAspectRatio="none">
    <defs>
      <linearGradient id="brushed" x1="0" y1="0" x2="1" y2="1">
        <stop offset="0" stop-color="#2c2c2c"/><stop offset=".5" stop-color="#4a4a4a"/><stop offset="1" stop-color="#1b1b1b"/>
      </linearGradient>
      <radialGradient id="seal" cx=".4" cy=".35" r=".7">
        <stop offset="0" stop-color="#f0c877"/><stop offset="1" stop-color="#8a5a1e"/>
      </radialGradient>
    </defs>
    <path class="card-body" role="img" aria-label="Dark brushed-metal card background" fill="url(#brushed)"
      d="M14 0H36Q170 70 304 0H326Q340 0 340 14V306Q340 320 326 320H304Q170 250 36 320H14Q0 320 0 306V14Q0 0 14 0Z"/>
    <line x1="0" y1="68" x2="340" y2="68" stroke="var(--fold-green)" stroke-dasharray="3 3"/>
    <line x1="0" y1="165" x2="340" y2="165" stroke="var(--fold-green)" stroke-dasharray="3 3" opacity=".6"/>
    <path class="hanger-hole" fill="#f2f2f2" d="M205 104C195 94 183 94 175 104C167 94 153 94 145 104L122 104L92 160L122 216L145 216C153 226 167 226 175 216C183 226 195 226 205 216C214 210 212 200 203 198L138 198L113 160L138 122L203 122C212 118 214 110 205 104Z"/>
    <text transform="translate(110 86) rotate(180)" font-family="Cinzel,serif" font-weight="700" font-size="8.5" fill="var(--gold-light)" text-anchor="middle">ABRASIVES &amp; ACCESSORIES</text>
    <g transform="translate(45 130) rotate(180)" font-family="PT Sans,sans-serif" font-weight="700" fill="var(--chrome)" text-anchor="middle">
      <text y="-12" font-size="12">LUMEN</text><text y="2" font-size="12">RIDGE</text>
    </g>
    <g font-family="PT Sans,sans-serif" font-weight="700" fill="var(--chrome)" text-anchor="middle">
      <text x="50" y="205" font-size="20">LUMEN</text><text x="50" y="228" font-size="20">RIDGE</text>
    </g>
    <text x="166" y="248" font-family="Cinzel,serif" font-weight="700" font-size="8.5" fill="var(--gold-light)" text-anchor="middle">ABRASIVES &amp; ACCESSORIES</text>
    <circle cx="42" cy="285" r="22" fill="url(#seal)" role="img" aria-label="Performance guarantee seal"/>
  </svg>
</div>

<div class="sticker-label">stiker</div>

<div class="sticker dark-text" style="left:434px;top:75px;--grade:var(--grade-yellow)">
  <div class="sticker-info">125mm x 8 HOLE P40<br>Product 123456</div><div class="sticker-code-area"></div>
  <div class="grade"><span class="grade-ring"></span>P40</div><div class="grade-rule"></div>
  <div class="sticker-desc"><b>125mm x 8 HOLE</b>SANDING DISKS</div><div class="sticker-notes"></div><div class="sticker-qty">QTY 5</div>
</div>
<div class="sticker dark-text" style="left:557px;top:75px;--grade:var(--grade-orange)">
  <div class="sticker-info">125mm x 8 HOLE P60<br>Product 123456</div><div class="sticker-code-area"></div>
  <div class="grade"><span class="grade-ring"></span>P60</div><div class="grade-rule"></div>
  <div class="sticker-desc"><b>125mm x 8 HOLE</b>SANDING DISKS</div><div class="sticker-notes"></div><div class="sticker-qty">QTY 5</div>
</div>
<div class="sticker dark-text" style="left:681px;top:75px;--grade:var(--grade-red)">
  <div class="sticker-info">125mm x 8 HOLE P80<br>Product 123456</div><div class="sticker-code-area"></div>
  <div class="grade"><span class="grade-ring"></span>P80</div><div class="grade-rule"></div>
  <div class="sticker-desc"><b>125mm x 8 HOLE</b>SANDING DISKS</div><div class="sticker-notes"></div><div class="sticker-qty">QTY 5</div>
</div>
<div class="sticker dark-text" style="left:807px;top:75px;--grade:var(--grade-teal)">
  <div class="sticker-info">125mm x 8 HOLE P120<br>Product 123456</div><div class="sticker-code-area"></div>
  <div class="grade"><span class="grade-ring"></span>P120</div><div class="grade-rule"></div>
  <div class="sticker-desc"><b>125mm x 8 HOLE</b>SANDING DISKS</div><div class="sticker-notes"></div><div class="sticker-qty">QTY 5</div>
</div>
<div class="sticker white-text" style="left:931px;top:75px;--grade:var(--grade-purple)">
  <div class="sticker-info">125mm x 8 HOLE P180<br>Product 123456</div><div class="sticker-code-area"></div>
  <div class="grade"><span class="grade-ring"></span>P180</div><div class="grade-rule"></div>
  <div class="sticker-desc"><b>125mm x 8 HOLE</b>SANDING DISKS</div><div class="sticker-notes"></div><div class="sticker-qty">QTY 5</div>
</div>
<div class="sticker dark-text" style="left:1054px;top:75px;--grade:var(--grade-magenta)">
  <div class="sticker-info">125mm x 8 HOLE P240<br>Product 123456</div><div class="sticker-code-area"></div>
  <div class="grade"><span class="grade-ring"></span>P240</div><div class="grade-rule"></div>
  <div class="sticker-desc"><b>125mm x 8 HOLE</b>SANDING DISKS</div><div class="sticker-notes"></div><div class="sticker-qty">QTY 5</div>
</div>

<!-- Assembled header cards -->
<div class="header-card card-a">
  <svg viewBox="0 0 340 320" preserveAspectRatio="none">
    <path role="img" aria-label="Dark brushed-metal card background" fill="url(#brushed)" stroke="#000" stroke-width="1.5"
      d="M14 0H36Q170 70 304 0H326Q340 0 340 14V306Q340 320 326 320H304Q170 250 36 320H14Q0 320 0 306V14Q0 0 14 0Z"/>
    <path fill="none" stroke="var(--die-pink)" stroke-width=".8" d="M20 8H40Q170 76 300 8H320Q332 8 332 20V300Q332 312 320 312H300Q170 244 40 312H20Q8 312 8 300V20Q8 8 20 8Z"/>
    <line x1="0" y1="75" x2="340" y2="75" stroke="#bbb" stroke-dasharray="2 3"/>
    <line x1="0" y1="158" x2="340" y2="158" stroke="var(--fold-red)" stroke-dasharray="3 3"/>
    <path fill="none" stroke="var(--die-pink)" stroke-dasharray="3 2" d="M205 104C195 94 183 94 175 104C167 94 153 94 145 104L122 104L92 160L122 216L145 216C153 226 167 226 175 216C183 226 195 226 205 216C214 210 212 200 203 198L138 198L113 160L138 122L203 122C212 118 214 110 205 104Z"/>
    <text transform="translate(110 88) rotate(180)" font-family="Cinzel,serif" font-weight="700" font-size="8.5" fill="var(--gold-light)" text-anchor="middle">ABRASIVES &amp; ACCESSORIES</text>
    <g transform="translate(45 132) rotate(180)" font-family="PT Sans,sans-serif" font-weight="700" fill="var(--chrome)" text-anchor="middle"><text y="-12" font-size="12">LUMEN</text><text y="2" font-size="12">RIDGE</text></g>
    <g font-family="PT Sans,sans-serif" font-weight="700" fill="var(--chrome)" text-anchor="middle"><text x="50" y="200" font-size="20">LUMEN</text><text x="50" y="223" font-size="20">RIDGE</text></g>
    <text x="166" y="244" font-family="Cinzel,serif" font-weight="700" font-size="8.5" fill="var(--gold-light)" text-anchor="middle">ABRASIVES &amp; ACCESSORIES</text>
    <circle cx="42" cy="280" r="22" fill="url(#seal)" role="img" aria-label="Performance guarantee seal"/>
  </svg>
</div>
<div class="sticker on-card light" style="left:293px;top:452px;--grade:var(--grade-orange)">
  <div class="sticker-info">125mm x 8 HOLE P80<br>Product 123456</div><div class="sticker-code-area"></div>
  <div class="grade"><span class="grade-ring"></span>P40</div><div class="grade-rule"></div>
  <div class="sticker-desc"><b>125mm x 8 HOLE</b>SANDING DISKS</div><div class="sticker-notes"></div><div class="sticker-qty">QTY 5</div>
</div>

<div class="header-card card-b">
  <svg viewBox="0 0 340 320" preserveAspectRatio="none">
    <path role="img" aria-label="Dark brushed-metal card background" fill="url(#brushed)" stroke="#000" stroke-width="1.5"
      d="M14 0H36Q170 70 304 0H326Q340 0 340 14V306Q340 320 326 320H304Q170 250 36 320H14Q0 320 0 306V14Q0 0 14 0Z"/>
    <path fill="none" stroke="var(--die-pink)" stroke-width=".8" d="M20 8H40Q170 76 300 8H320Q332 8 332 20V300Q332 312 320 312H300Q170 244 40 312H20Q8 312 8 300V20Q8 8 20 8Z"/>
    <line x1="0" y1="75" x2="340" y2="75" stroke="#bbb" stroke-dasharray="2 3"/>
    <line x1="0" y1="158" x2="340" y2="158" stroke="var(--fold-red)" stroke-dasharray="3 3"/>
    <path fill="none" stroke="var(--die-pink)" stroke-dasharray="3 2" d="M205 104C195 94 183 94 175 104C167 94 153 94 145 104L122 104L92 160L122 216L145 216C153 226 167 226 175 216C183 226 195 226 205 216C214 210 212 200 203 198L138 198L113 160L138 122L203 122C212 118 214 110 205 104Z"/>
    <text transform="translate(110 88) rotate(180)" font-family="Cinzel,serif" font-weight="700" font-size="8.5" fill="var(--gold-light)" text-anchor="middle">ABRASIVES &amp; ACCESSORIES</text>
    <g transform="translate(45 132) rotate(180)" font-family="PT Sans,sans-serif" font-weight="700" fill="var(--chrome)" text-anchor="middle"><text y="-12" font-size="12">LUMEN</text><text y="2" font-size="12">RIDGE</text></g>
    <g font-family="PT Sans,sans-serif" font-weight="700" fill="var(--chrome)" text-anchor="middle"><text x="50" y="200" font-size="20">LUMEN</text><text x="50" y="223" font-size="20">RIDGE</text></g>
    <text x="166" y="244" font-family="Cinzel,serif" font-weight="700" font-size="8.5" fill="var(--gold-light)" text-anchor="middle">ABRASIVES &amp; ACCESSORIES</text>
    <circle cx="42" cy="280" r="22" fill="url(#seal)" role="img" aria-label="Performance guarantee seal"/>
  </svg>
</div>
<div class="sticker on-card light" style="left:670px;top:452px;--grade:var(--grade-red)">
  <div class="sticker-info">125mm x 8 HOLE P80<br>Product 123456</div><div class="sticker-code-area"></div>
  <div class="grade"><span class="grade-ring"></span>P80</div><div class="grade-rule"></div>
  <div class="sticker-desc"><b>125mm x 8 HOLE</b>SANDING DISKS</div><div class="sticker-notes"></div><div class="sticker-qty">QTY 5</div>
</div>

<div class="header-card card-c">
  <svg viewBox="0 0 340 320" preserveAspectRatio="none">
    <path role="img" aria-label="Dark brushed-metal card background" fill="url(#brushed)" stroke="#000" stroke-width="1.5"
      d="M14 0H36Q170 70 304 0H326Q340 0 340 14V306Q340 320 326 320H304Q170 250 36 320H14Q0 320 0 306V14Q0 0 14 0Z"/>
    <path fill="none" stroke="var(--die-pink)" stroke-width=".8" d="M20 8H40Q170 76 300 8H320Q332 8 332 20V300Q332 312 320 312H300Q170 244 40 312H20Q8 312 8 300V20Q8 8 20 8Z"/>
    <line x1="0" y1="75" x2="340" y2="75" stroke="#bbb" stroke-dasharray="2 3"/>
    <line x1="0" y1="158" x2="340" y2="158" stroke="var(--fold-red)" stroke-dasharray="3 3"/>
    <path fill="none" stroke="var(--die-pink)" stroke-dasharray="3 2" d="M205 104C195 94 183 94 175 104C167 94 153 94 145 104L122 104L92 160L122 216L145 216C153 226 167 226 175 216C183 226 195 226 205 216C214 210 212 200 203 198L138 198L113 160L138 122L203 122C212 118 214 110 205 104Z"/>
    <text transform="translate(110 88) rotate(180)" font-family="Cinzel,serif" font-weight="700" font-size="8.5" fill="var(--gold-light)" text-anchor="middle">ABRASIVES &amp; ACCESSORIES</text>
    <g transform="translate(45 132) rotate(180)" font-family="PT Sans,sans-serif" font-weight="700" fill="var(--chrome)" text-anchor="middle"><text y="-12" font-size="12">LUMEN</text><text y="2" font-size="12">RIDGE</text></g>
    <g font-family="PT Sans,sans-serif" font-weight="700" fill="var(--chrome)" text-anchor="middle"><text x="50" y="200" font-size="20">LUMEN</text><text x="50" y="223" font-size="20">RIDGE</text></g>
    <text x="166" y="244" font-family="Cinzel,serif" font-weight="700" font-size="8.5" fill="var(--gold-light)" text-anchor="middle">ABRASIVES &amp; ACCESSORIES</text>
    <circle cx="42" cy="280" r="22" fill="url(#seal)" role="img" aria-label="Performance guarantee seal"/>
  </svg>
</div>
<div class="sticker on-card" style="left:1047px;top:452px;--grade:var(--grade-purple)">
  <div class="sticker-info">125mm x 8 HOLE P80<br>Product 123456</div><div class="sticker-code-area"></div>
  <div class="grade"><span class="grade-ring"></span>P180</div><div class="grade-rule"></div>
  <div class="sticker-desc"><b>125mm x 8 HOLE</b>SANDING DISKS</div><div class="sticker-notes"></div><div class="sticker-qty">QTY 5</div>
</div>

</body>
</html>
```